Postcard Design hearing aid sales & service. Free hearing test . Fresh batteries

Bluebonnet Hearing Aid Device Center . Located at 417 Marwick Ln Abilene Texas 79488 Ph 325-555-0147.
Hours Mon thru Thurs 9:00am - 5:00pm closed for lunch 12:00pm - 1:00pm . Fri open 9:00am - 1:00pm
Hearing Test n/c Hearing aid adjustment & cleaning of hearing aids n/c . Fresh batteries buy one 1/2 off on 2nd pack. Limited time. Walk-in welcome Appointments appreciated. THIS MONTH ONLY Special discounts on new state of the art hearing aids w/remote. .

```html
<!DOCTYPE html>
<html lang="en">
<head>
<meta charset="utf-8">
<title>Bluebonnet Hearing Aids – Postcard</title>
<link rel="stylesheet" href="https://fonts.googleapis.com/css2?family=Oswald:wght@500&family=Lato:wght@400;700&family=Roboto+Condensed:wght@400&display=swap">
<style>
  :root {
    --navy: #1d4c80;
    --navy-deep: #163e6b;
    --beige: #d9d1bd;
    --beige-light: #ece7da;
    --paper: #ffffff;
    --paper-soft: #f1f1f1;
    --ink: #2b2b2b;
    --ink-soft: #4a4a4a;
    --stage: #e4e2de;
    --stamp: #d9d9d9;
  }
  * { box-sizing: border-box; margin: 0; padding: 0; }
  html, body { width: 900px; height: 1200px; overflow: hidden; }
  body { background: var(--stage); position: relative; font-family: "Lato", sans-serif; color: var(--ink); }

  .card { position: absolute; left: 123px; width: 655px; background: var(--paper); overflow: hidden; box-shadow: 0 3px 10px rgba(0,0,0,.25); }
  .card--front { top: 72px; height: 508px; }
  .card--back  { top: 646px; height: 507px; }
  .card__art { position: absolute; inset: 0; width: 100%; height: 100%; }
  .card__text { position: absolute; }

  .headline { font-family: "Oswald", sans-serif; font-weight: 500; color: var(--paper); text-transform: uppercase; letter-spacing: .2px; white-space: nowrap; }

  .front__title { left: 335px; top: 26px; width: 310px; text-align: center; font-size: 25px; line-height: 34px; }
  .front__hours { right: 28px; top: 115px; text-align: right; font-size: 16.5px; line-height: 22px; color: var(--ink); white-space: nowrap; }
  .front__hours .hours__lunch { color: var(--navy); }
  .front__offer { right: 30px; top: 226px; text-align: right; font-family: "Oswald", sans-serif; font-weight: 500; font-size: 17px; line-height: 24px; text-transform: uppercase; white-space: nowrap; }
  .front__offer .offer__lead { color: var(--navy); }
  .front__offer .offer__tail { color: var(--ink); }
  .front__services { left: 28px; top: 290px; list-style: none; font-family: "Roboto Condensed", sans-serif; font-size: 16px; line-height: 23px; color: var(--ink); white-space: nowrap; }
  .front__services li::before { content: ""; display: inline-block; width: 8px; height: 8px; border-radius: 50%; background: var(--navy); margin-right: 8px; vertical-align: 2px; }

  .brand { left: 386px; top: 383px; display: flex; align-items: center; }
  .brand__name { font-family: "Lato", sans-serif; font-weight: 400; font-size: 20px; line-height: 22px; color: var(--ink-soft); width: 125px; }
  .brand__rule { width: 3px; height: 50px; background: var(--navy); margin: 0 8px 0 6px; }
  .brand__tag { font-size: 11px; line-height: 15px; color: var(--navy); width: 110px; }

  .web { font-family: "Lato", sans-serif; color: var(--paper); letter-spacing: 1px; white-space: nowrap; }
  .front__web { right: 26px; top: 466px; font-size: 19px; }

  .back__intro { left: 22px; top: 38px; width: 290px; font-size: 10.5px; line-height: 14px; color: var(--ink-soft); }
  .back__title { left: 24px; top: 132px; font-size: 21px; line-height: 30px; }
  .back__title .title__sub { font-size: 14.5px; line-height: 22px; display: block; }
  .back__contact { left: 38px; top: 326px; font-size: 21px; line-height: 28px; color: var(--ink-soft); white-space: nowrap; }
  .back__contact .contact__city { color: var(--navy); font-weight: 700; }
  .back__web { left: 42px; top: 457px; font-size: 16.5px; }
</style>
</head>
<body>

<section class="card card--front" aria-label="Postcard front">
  <svg class="card__art" viewBox="0 0 655 508">
    <defs>
      <linearGradient id="frontBg" x1="0" y1="0" x2="0" y2="1">
        <stop offset="0" stop-color="#ffffff"/>
        <stop offset="1" stop-color="#e9e9e9"/>
      </linearGradient>
      <linearGradient id="photoTone" x1="0" y1="0" x2="1" y2="1">
        <stop offset="0" stop-color="#d8bf9e"/>
        <stop offset=".5" stop-color="#efe6dc"/>
        <stop offset="1" stop-color="#c9ccd2"/>
      </linearGradient>
      <linearGradient id="thumbTone" x1="0" y1="0" x2="1" y2="1">
        <stop offset="0" stop-color="#eee2cf"/>
        <stop offset="1" stop-color="#cfd3d8"/>
      </linearGradient>
      <clipPath id="frontClip"><rect width="655" height="508"/></clipPath>
    </defs>
    <g clip-path="url(#frontClip)">
      <rect width="655" height="508" fill="url(#frontBg)"/>
      <path d="M0 170 H255 C335 200 350 300 312 450 H0 Z" fill="var(--beige)"/>
      <path d="M330 0 H655 V88 C560 78 430 86 330 112 Z" fill="var(--navy)"/>
      <path d="M330 112 C430 86 560 78 655 88 V180 C560 200 440 190 330 205 Z" fill="var(--beige-light)"/>
      <path d="M305 186 C365 250 362 360 310 450" fill="none" stroke="var(--navy)" stroke-width="4"/>
      <g role="img" aria-label="Photo: a hearing specialist checks a young girl's ear while her mother comforts her">
        <circle cx="160" cy="112" r="170" fill="url(#photoTone)"/>
      </g>
      <circle cx="160" cy="112" r="170" fill="none" stroke="var(--navy)" stroke-width="5"/>
      <g role="img" aria-label="Photo: hands holding two hearing aids shaped into a heart">
        <rect x="394" y="287" width="231" height="74" fill="#d9dde2" stroke="var(--navy)" stroke-width="2"/>
      </g>
      <path d="M0 450 H300 C340 445 360 438 380 436 H655 V508 H0 Z" fill="var(--navy)"/>
      <g role="img" aria-label="Photo: coloured foam ear plugs">
        <circle cx="90" cy="420" r="44" fill="url(#thumbTone)" stroke="var(--navy)" stroke-width="4"/>
        <circle cx="90" cy="420" r="49" fill="none" stroke="#ffffff" stroke-width="3"/>
      </g>
      <g role="img" aria-label="Photo: behind-the-ear hearing aid">
        <circle cx="214" cy="420" r="44" fill="url(#thumbTone)" stroke="var(--navy)" stroke-width="4"/>
        <circle cx="214" cy="420" r="49" fill="none" stroke="#ffffff" stroke-width="3"/>
      </g>
    </g>
  </svg>

  <h1 class="card__text headline front__title">Bluebonnet Hearing Aids</h1>
  <p class="card__text front__hours">
    Mon thru Thurs 9:00am - 5:00pm<br>
    <span class="hours__lunch">Closed for lunch 12:00pm - 1:00pm</span><br>
    Fri open 9:00am - 1:00pm
  </p>
  <p class="card__text front__offer">
    <span class="offer__lead">Fresh batteries buy one 1/2 off</span><br>
    <span class="offer__tail">on 2nd pack for limited time</span>
  </p>
  <ul class="card__text front__services">
    <li>Hearing Test n/c Hearing aid adjustment</li>
    <li>Cleaning of hearing aids n/c</li>
    <li>Walk-in welcome Appointments appreciated</li>
  </ul>
  <div class="card__text brand">
    <span class="brand__name">Bluebonnet Hearing Aids</span>
    <span class="brand__rule"></span>
    <span class="brand__tag">Online Guide to Hearing Aid Stores in Texas</span>
  </div>
  <p class="card__text web front__web">www.bluebonnethearing.example</p>
</section>

<section class="card card--back" aria-label="Postcard back">
  <svg class="card__art" viewBox="0 0 655 507">
    <defs>
      <linearGradient id="backThumb" x1="0" y1="0" x2="1" y2="1">
        <stop offset="0" stop-color="#e9cdb4"/>
        <stop offset="1" stop-color="#cfd4da"/>
      </linearGradient>
    </defs>
    <rect width="655" height="507" fill="var(--paper)"/>
    <path d="M0 0 H300 C340 20 360 60 370 100 H0 Z" fill="var(--beige-light)"/>
    <path d="M0 215 H382 C374 300 350 380 318 430 H0 Z" fill="var(--beige)"/>
    <path d="M0 100 H384 C394 140 396 180 386 215 H0 Z" fill="var(--navy)"/>
    <path d="M388 100 C402 160 398 280 322 430" fill="none" stroke="var(--navy)" stroke-width="4"/>
    <rect x="565" y="30" width="62" height="62" fill="var(--stamp)"/>
    <rect x="0" y="430" width="655" height="8" fill="var(--navy)"/>
    <rect x="0" y="430" width="325" height="77" fill="var(--navy)"/>
    <g role="img" aria-label="Photo: a hand cupped behind an ear">
      <circle cx="70" cy="251" r="43" fill="url(#backThumb)" stroke="var(--navy)" stroke-width="4"/>
      <circle cx="70" cy="251" r="48" fill="none" stroke="#ffffff" stroke-width="3"/>
    </g>
    <g role="img" aria-label="Photo: an ear being examined with an otoscope">
      <circle cx="188" cy="251" r="43" fill="url(#backThumb)" stroke="var(--navy)" stroke-width="4"/>
      <circle cx="188" cy="251" r="48" fill="none" stroke="#ffffff" stroke-width="3"/>
    </g>
    <g role="img" aria-label="Photo: an older woman being fitted with a hearing aid">
      <circle cx="304" cy="251" r="43" fill="url(#backThumb)" stroke="var(--navy)" stroke-width="4"/>
      <circle cx="304" cy="251" r="48" fill="none" stroke="#ffffff" stroke-width="3"/>
    </g>
  </svg>

  <p class="card__text back__intro">If you're seeking to buy hearing aids in Texas with a minimum of fuss and worry, look no further. That's what Bluebonnet Hearing Aids is all about.</p>
  <h2 class="card__text headline back__title">This month only special discounts<span class="title__sub">on new state of the art hearing aids w/remote</span></h2>
  <p class="card__text back__contact">
    Located at 417 Marwick<br>
    <span class="contact__city">Ln Abilene Texas 79488</span><br>
    Call us: 325-555-0147
  </p>
  <p class="card__text web back__web">www.bluebonnethearing.example</p>
</section>

</body>
</html>
```